Orlo Novelties

We need a web design for an ecommerce website that sells innovative gadgets. ***We are in the early stages of the business and don't have official products yet, they are being created. so we need to use placeholders and fake content, please email me with any questions regarding this.

The web page must look modern, fresh and simple and include-

• Logo
• My Account & View Cart link
• Menu - Home, Shop, The Latest, About Us, FAQ, Blog, Contact Us
• Promo bar at the top of the page like on: http://www.larkandfern.com/lkfn/ (you can use placeholder text for now)
• Search Box
• Chatterloom, Quipsy, Vidarrow, Snipboard and Orbix+ icons
• Slogan “Amaze your friends”
• Free shipping on orders over $50
• Banner section - for now you can highlight one of the fake products below, focus on free shipping on order over $50 or some kind of fake promotion
• New Arrivals section - highlight these fake products since we don't have products yet so you can use these products as place holders-
1. https://www.thebramblecart.com/tech-gadgets/the-zuvvet
2. https://www.thebramblecart.com/tech-gadgets/plinzo-cord-keeper
3. https://www.thebramblecart.com/tech-gadgets/ventrosk-padsofts
• credit card logos
• payvoucha.net seal - https://check.payvoucha.net/pvseal/images/secure90x72.gif

Example websites:
http://www.larkandfern.com/lkfn/
https://www.thebramblecart.com/
http://www.velmstacks.com/
https://plovewick.co/
http://zentrioworks.com/
http://www.dulvaroltd.com/
http://www.quessary.com/

• • Logo
• Search Box
• credit card logos

```html
<!DOCTYPE html>
<html lang="en">
<head>
<meta charset="utf-8">
<title>Orlo Novelties</title>
<link rel="stylesheet" href="https://fonts.googleapis.com/css2?family=Roboto:wght@400;500;700&family=Roboto+Slab:wght@400&display=swap">
<style>
:root{
  --navy:#0f2b5b;
  --sky:#4bbde9;
  --sky-text:#4fb3dd;
  --red:#c8282c;
  --red-dark:#a51d22;
  --grey-bg:#efefef;
  --footer-bg:#ebebeb;
  --text:#333;
}
*{box-sizing:border-box;margin:0;padding:0}
html,body{width:926px;height:1200px;overflow:hidden}
body{position:relative;font-family:"Roboto",sans-serif;color:var(--text);background:#fff}
.abs{position:absolute}
a{color:inherit;text-decoration:none}

.promo-bar{left:0;top:0;width:926px;height:34px;background:var(--navy);color:#fff;font-size:8.4px;display:flex;align-items:center;justify-content:center}

.header{left:0;top:34px;width:926px;height:104px;background:#fff}
.shipping-note{left:133px;top:34px;display:flex;align-items:center;gap:14px}
.shipping-note .truck-photo{width:54px;height:40px;border-radius:4px;background:radial-gradient(ellipse at 45% 45%,#d23a3c 0%,#c8282c 40%,rgba(200,40,44,.25) 70%,rgba(255,255,255,0) 85%)}
.shipping-note strong{display:block;font-weight:400;font-size:16.5px;color:#333;line-height:20px}
.shipping-note span{font-size:11.5px;color:#444}
.brand{left:380px;top:14px;width:156px;text-align:center}
.brand .mark{display:flex;align-items:center;justify-content:center;gap:6px;margin-top:26px}
.brand .dot{width:18px;height:18px;border-radius:50%;background:var(--sky)}
.brand .name{font-size:18px;font-weight:500;color:var(--navy)}
.brand .slogan{font-size:10.5px;color:#333;margin-top:10px}
.account-links{left:617px;top:30px;font-size:10px;color:#333;display:flex;gap:7px;align-items:center}
.account-links .cart-total{color:var(--navy);margin-left:-4px}
.search{left:615px;top:55px;width:175px;height:27px;display:flex;border:1px solid #c9c9c9;border-radius:3px;overflow:hidden;box-shadow:inset 0 1px 2px rgba(0,0,0,.15)}
.search input{flex:1;border:0;font:8px "Roboto",sans-serif;padding-left:8px;color:#555;background:#fff}
.search button{width:28px;border:0;background:var(--navy);display:flex;align-items:center;justify-content:center}

.main-nav{left:0;top:138px;width:926px;height:47px;background:var(--sky)}
.main-nav ul{list-style:none;position:absolute;left:132px;top:0;height:47px;display:flex}
.main-nav li{height:47px;display:flex;align-items:center;justify-content:center;color:#fff;font-size:12.5px;border-right:1px solid rgba(255,255,255,.35)}
.main-nav li:last-child{border-right:0}
.main-nav li.active{background:var(--navy)}

.stage{left:0;top:185px;width:926px;height:355px;background:var(--grey-bg)}
.hero{left:132px;top:185px;width:660px;height:354px;background:radial-gradient(ellipse at 35% 35%,#ffffff 0%,#e9f5fc 55%,#cfe9f6 100%);border:1px solid #d6e3ea;overflow:hidden}
.hero h1{position:absolute;left:60px;top:128px;font:400 26px "Roboto Slab",serif;color:var(--navy);white-space:nowrap}
.hero p{position:absolute;left:60px;top:174px;font:400 15.5px "Roboto Slab",serif;color:var(--sky-text);white-space:nowrap}
.btn{display:inline-flex;align-items:center;justify-content:center;background:linear-gradient(#d8383b,var(--red-dark));color:#fff;font-weight:500;border-radius:3px;border:1px solid #9c1b1f}
.hero .btn{position:absolute;left:60px;top:208px;width:92px;height:26px;font-size:10.5px}
.hero .product-photo{position:absolute;left:350px;top:36px;width:270px;height:290px;background:radial-gradient(ellipse at 50% 45%,#45484e 0%,#3a3c41 38%,rgba(58,60,65,.55) 55%,rgba(207,233,246,0) 72%)}
.hero .arrow{position:absolute;top:150px;width:14px;height:40px}

.section-title{left:0;top:560px;width:926px;text-align:center;font:400 16.5px "Roboto Slab",serif;color:var(--navy)}
.card{top:600px;width:215px;height:198px;border:3px solid #fff;box-shadow:0 0 0 1px #d9d9d9,0 14px 14px -10px rgba(0,0,0,.25);background:radial-gradient(ellipse at 50% 40%,#fff 45%,#d9e1ef 100%)}
.card .photo{position:absolute;left:30px;top:14px;width:155px;height:118px}
.card h3{position:absolute;left:27px;font-size:11px;font-weight:400;color:#111;white-space:nowrap}
.card .price{position:absolute;left:27px;top:163px;font-size:12px;color:var(--red)}
.card .btn{position:absolute;right:22px;top:157px;width:53px;height:21px;font-size:7.5px}

.divider{left:135px;top:853px;width:654px;height:1px;background:#bdbdbd}
.press{left:144px;top:860px;width:621px;height:68px;background:#f6f5f1;display:flex;align-items:center;justify-content:space-around;font-weight:700;color:#222}
.press span{font-size:15px}

.footer{left:0;top:928px;width:926px;height:183px;background:var(--footer-bg)}
.col h4{font-weight:400;font-size:14.5px;color:var(--navy);margin-bottom:14px}
.col p,.col li{font-size:9.6px;color:#444;line-height:16.5px;list-style:none}
.vline{top:965px;width:1px;height:135px;background:#c2c2c2}
.newsletter-input{width:153px;height:23px;background:#fff;border:1px solid #bbb;margin-top:8px;position:relative}
.newsletter-input svg{position:absolute;right:5px;top:7px}
.cards{display:flex;gap:5px;margin-top:10px}
.cards span{width:27px;height:17px;border-radius:2px;font-size:5px;font-weight:700;color:#fff;display:flex;align-items:center;justify-content:center}
.social-plugin{left:668px;top:963px;width:124px}
.social-plugin .pname{font-size:7px;font-weight:500;color:var(--navy);display:flex;align-items:center;gap:4px}
.social-plugin .pname i{width:9px;height:9px;border-radius:50%;background:var(--sky);display:block}
.social-plugin .likes{font-size:5.6px;color:#555;margin:6px 0 4px;border-bottom:1px solid #ddd;padding-bottom:3px}
.social-plugin .fans{display:grid;grid-template-columns:repeat(4,28px);gap:2px}
.social-plugin .fans div{height:28px}
.social-plugin .plugin-note{font-size:5.2px;color:#777;margin-top:5px;border-top:1px solid #ddd;padding-top:3px}

.bottom-bar{left:0;top:1111px;width:926px;height:89px;background:var(--navy)}
.seal{left:133px;top:1133px;width:54px;height:45px;border-radius:50%;background:radial-gradient(circle,#f3d56a,#c99a1e)}
.copyright{left:0;top:1157px;width:926px;text-align:center;color:#fff;font-size:9.6px}
.social-row{left:592px;top:1146px;width:200px;display:flex;justify-content:space-between;color:#fff;font-size:5.6px}
.social-row span{width:40px;display:flex;flex-direction:column;align-items:center;gap:3px}
.social-row i{width:22px;height:22px;border-radius:50%;border:2px solid #fff;display:block}
</style>
</head>
<body>

<div class="abs promo-bar">Extended! Super Clip $20, Portable Video Projector $25, Royal Blue Padsofts $29, Super Clip $39 &amp; Up &amp; 40% Off Everything Else + Free Shipping Over $50. Click for Details.</div>

<header class="abs header">
  <div class="abs shipping-note">
    <div class="truck-photo" role="img" aria-label="Photo of a red delivery truck"></div>
    <div><strong>Free shipping</strong><span>on orders over $50</span></div>
  </div>
  <div class="abs brand">
    <div class="mark"><span class="dot"></span><span class="name">Orlo Novelties</span></div>
    <div class="slogan">Amaze your friends</div>
  </div>
  <div class="abs account-links">
    <a href="#">Login</a><span>|</span><a href="#">My Account</a><span>|</span>
    <a href="#">Cart</a>
    <svg width="13" height="11" viewBox="0 0 13 11" aria-hidden="true"><path d="M0 1h2.5l1.8 6h6.5L12 3H3.5" fill="none" stroke="#0f2b5b" stroke-width="1.2"/><circle cx="5" cy="9.5" r="1" fill="#0f2b5b"/><circle cx="10" cy="9.5" r="1" fill="#0f2b5b"/></svg>
    <span class="cart-total">: 0.00</span>
  </div>
  <form class="abs search">
    <input type="text" placeholder="Search" aria-label="Search">
    <button type="button" aria-label="Search">
      <svg width="13" height="13" viewBox="0 0 13 13"><circle cx="5.5" cy="5.5" r="4" fill="none" stroke="#fff" stroke-width="1.6"/><path d="M8.5 8.5l3.5 3.5" stroke="#fff" stroke-width="1.8"/></svg>
    </button>
  </form>
</header>

<nav class="abs main-nav">
  <ul>
    <li class="active" style="width:75px">HOME</li>
    <li style="width:84px">SHOP</li>
    <li style="width:125px">THE LATEST</li>
    <li style="width:106px">ABOUT US</li>
    <li style="width:72px">FAQ</li>
    <li style="width:81px">BLOG</li>
    <li style="width:117px">CONTACT US</li>
  </ul>
</nav>

<div class="abs stage"></div>
<section class="abs hero">
  <svg class="arrow" style="left:22px" viewBox="0 0 14 40" aria-label="Previous"><path d="M12 1L2 20l10 19" fill="none" stroke="#333" stroke-width="1"/></svg>
  <h1>INNOVATIVE GADGETS</h1>
  <p>FREE SHIPPING ON ORDER OVER $50</p>
  <a class="btn" href="#">BUY NOW</a>
  <div class="product-photo" role="img" aria-label="Photo of a dark grey ski helmet with built-in headphones"></div>
  <svg class="arrow" style="left:624px" viewBox="0 0 14 40" aria-label="Next"><path d="M2 1l10 19L2 39" fill="none" stroke="#333" stroke-width="1"/></svg>
</section>

<h2 class="abs section-title">NEW ARRIVALS</h2>

<article class="abs card" style="left:132px">
  <div class="photo" role="img" aria-label="Photo of four metal hook clips in silver, blue, red and black" style="background:radial-gradient(ellipse at 50% 50%,#8a96a6 0%,#b7c0cc 35%,rgba(255,255,255,0) 72%)"></div>
  <h3 style="top:137px">Super Clip</h3>
  <div class="price">$20</div>
  <a class="btn" href="#">BUY NOW</a>
</article>
<article class="abs card" style="left:354px">
  <div class="photo" role="img" aria-label="Photo of a black cardboard smartphone projector box" style="background:radial-gradient(ellipse at 50% 45%,#2d2d2f 0%,#49494c 35%,rgba(255,255,255,0) 68%)"></div>
  <h3 style="top:142px">Portable Video Projector</h3>
  <div class="price">$20</div>
  <a class="btn" href="#">BUY NOW</a>
</article>
<article class="abs card" style="left:577px">
  <div class="photo" role="img" aria-label="Photo of royal blue foam headphones" style="background:radial-gradient(ellipse at 50% 45%,#1f4fd8 0%,#3563e0 35%,rgba(255,255,255,0) 68%)"></div>
  <h3 style="top:141px">Royal Blue Padsofts</h3>
  <div class="price">$20</div>
  <a class="btn" href="#">BUY NOW</a>
</article>

<div class="abs divider"></div>
<div class="abs press" aria-label="As featured in">
  <span>MORNING</span><span>All Gadget Report</span><span>Better Nests</span><span>Fenwick</span><span>StartupPulse</span>
</div>

<footer class="abs footer"></footer>
<div class="abs vline" style="left:293px"></div>
<div class="abs vline" style="left:445px"></div>
<div class="abs vline" style="left:646px"></div>

<div class="abs col" style="left:132px;top:963px;width:150px">
  <h4>CONTACT US</h4>
  <p style="padding-left:2px">Lorem Ipsum has been the standard dummy text ever since when an unknown printer<br>Tel 010-5530912<br>Email info@orlonovelties.com</p>
</div>
<div class="abs col" style="left:320px;top:963px">
  <h4>MY ACCOUNT</h4>
  <ul style="padding-left:6px"><li>Your Account</li><li>My orders</li><li>My credit slips</li><li>My addresses</li><li>Login</li></ul>
</div>
<div class="abs col" style="left:474px;top:963px">
  <h4>NEWSLETTER</h4>
  <p>Sign Up for Our Newsletter:</p>
  <div class="newsletter-input"><svg width="6" height="9" viewBox="0 0 6 9"><path d="M0 0l6 4.5L0 9z" fill="#333"/></svg></div>
  <p style="margin-top:9px">Payment</p>
  <div class="cards">
    <span style="background:#f2b632">Paylark</span>
    <span style="background:#e8a81e">eTrove</span>
    <span style="background:#2f6db5">Nimbex</span>
    <span style="background:#c8282c">MeridCard</span>
    <span style="background:#1d3f8f">Vistrao</span>
  </div>
</div>
<div class="abs social-plugin">
  <div class="pname"><i></i>Orlo Novelties</div>
  <div class="likes">32,742 people like Orlo Novelties.</div>
  <div class="fans" role="img" aria-label="Grid of fan profile pictures">
    <div style="background:#c9b3ad"></div><div style="background:#d4d8e3"></div><div style="background:#cbbfa9"></div><div style="background:#a08476"></div>
    <div style="background:#b8a7a6"></div><div style="background:#8e78b0"></div><div style="background:#d6b5a3"></div><div style="background:#b94a3a"></div>
  </div>
  <div class="plugin-note">Chatterloom social plugin</div>
</div>

<div class="abs bottom-bar"></div>
<div class="abs seal" role="img" aria-label="payvoucha.net verified merchant seal"></div>
<div class="abs copyright">© Copyright 2014 &nbsp; All Rights Reserved</div>
<div class="abs social-row">
  <span><i style="background:#c8282c"></i>Snipboard</span>
  <span><i style="background:#3b5a9a"></i>Chatterloom</span>
  <span><i style="background:#d9473b"></i>Orbix+</span>
  <span><i style="background:#2aa3e0"></i>Quipsy</span>
  <span><i style="background:#c4302b"></i>Vidarrow</span>
</div>

</body>
</html>
```